Modern Dry eye Poster for eye center, Optometrist office

We need a banner to connect to patient about dry eye and treatment. Ask if patient has dry eyes and we offer treatment .
What is dry eye?
Are you suffering for dry, gritty, painful eyes, blurred vision, redness..

Now there is a quick, comfortable and affordable procedure offering relief tofdry eye.

Schedule your dry eye treatment today.

Target Market(s)

Dry eye patient

Font styles to use
Sans Serif

Colors
00a990
ffffff
0492cd
fbf289
85cae6

Requirements
Must have
• Modern design, dry eye patient
Nice to have
• real life model of nice eyes
Should not have
• No cartoon,

```html
<!DOCTYPE html>
<html lang="en">
<head>
<meta charset="utf-8">
<title>Dry Eye Treatment Poster</title>
<link rel="stylesheet" href="https://fonts.googleapis.com/css2?family=Montserrat:wght@300;600;700;800;900&display=swap">
<style>
  :root {
    --yellow: #f9d511;
    --white: #ffffff;
    --ink: #1c1c1c;
    --red: #e30613;
    --violet: #b0468c;
    --grey: #555555;
    --frame: #222222;
  }
  html, body {
    margin: 0;
    padding: 0;
    width: 1094px;
    height: 1200px;
    overflow: hidden;
    background: var(--white);
    font-family: "Montserrat", sans-serif;
  }
  .poster {
    position: absolute;
    left: 123px;
    top: 0;
    width: 848px;
    height: 1200px;
    box-sizing: border-box;
    border: 2px solid var(--frame);
    background: var(--white);
    overflow: hidden;
  }
  .poster-art {
    position: absolute;
    inset: 0;
    width: 100%;
    height: 100%;
  }
  .headline text { font-family: "Montserrat", sans-serif; }
  .offer {
    position: absolute;
    left: 372px;
    top: 902px;
    width: 400px;
    color: var(--ink);
    font-weight: 600;
    font-size: 25px;
    line-height: 31px;
    text-transform: uppercase;
  }
  .offer-lead { margin: 0; }
  .offer-focus {
    margin: 4px 0 0;
    color: var(--red);
    font-size: 42px;
    line-height: 48px;
    font-weight: 600;
  }
  .offer-rule {
    margin: 8px 0 10px;
    width: 386px;
    height: 3px;
    background: var(--ink);
    border: 0;
  }
  .offer-cta {
    margin: 0;
    color: var(--red);
    font-weight: 700;
    font-size: 26px;
    line-height: 31px;
    letter-spacing: -0.5px;
  }
  .brand {
    position: absolute;
    left: 50px;
    top: 1098px;
    width: 230px;
    text-align: center;
    color: var(--grey);
    font-weight: 300;
    font-size: 28px;
    line-height: 30px;
    letter-spacing: 1px;
    text-transform: uppercase;
  }
  .brand-sub { display: block; font-size: 20px; letter-spacing: 3px; }
</style>
</head>
<body>
  <main class="poster">
    <svg class="poster-art" viewBox="0 0 848 1200" xmlns="http://www.w3.org/2000/svg">
      <defs>
        <linearGradient id="dryTexture" x1="0" y1="0" x2="1" y2="1">
          <stop offset="0" stop-color="#a7712e"/>
          <stop offset="0.45" stop-color="#c9a06a"/>
          <stop offset="0.7" stop-color="#8d8a86"/>
          <stop offset="1" stop-color="#b48855"/>
        </linearGradient>
        <linearGradient id="devicePhoto" x1="0" y1="0" x2="1" y2="1">
          <stop offset="0" stop-color="#cfe3f2"/>
          <stop offset="0.5" stop-color="#8fb3d6"/>
          <stop offset="1" stop-color="#9a9fa6"/>
        </linearGradient>
        <filter id="softShadow" x="-10%" y="-10%" width="130%" height="140%">
          <feDropShadow dx="6" dy="8" stdDeviation="5" flood-color="#000" flood-opacity="0.55"/>
        </filter>
        <filter id="blurText" x="-5%" y="-20%" width="110%" height="140%">
          <feGaussianBlur stdDeviation="3.2"/>
        </filter>
      </defs>

      <path class="band-yellow" fill="var(--yellow)"
            d="M0 0 H848 V860 C760 858 660 850 520 830 C380 810 300 740 160 736 C80 734 30 745 0 756 Z"/>

      <g class="headline">
        <text x="110" y="123" font-size="50" font-weight="600" fill="var(--ink)"
              textLength="630" lengthAdjust="spacingAndGlyphs">ARE YOU SUFFERING FOR</text>
        <text role="img" aria-label="dry eye, lettering filled with a cracked dry earth photo and a close-up of a blue eye"
              x="70" y="300" font-size="195" font-weight="900" fill="url(#dryTexture)"
              textLength="699" lengthAdjust="spacingAndGlyphs">dry eye</text>
        <text x="225" y="400" font-size="150" font-weight="900" fill="var(--white)"
              stroke="var(--ink)" stroke-width="5" paint-order="stroke" filter="url(#softShadow)"
              textLength="414" lengthAdjust="spacingAndGlyphs">gritty</text>
        <text x="70" y="512" font-size="125" font-weight="900" fill="var(--ink)"
              textLength="652" lengthAdjust="spacingAndGlyphs">painful eyes</text>
        <text x="100" y="595" font-size="110" font-weight="900" fill="var(--violet)" filter="url(#blurText)"
              textLength="656" lengthAdjust="spacingAndGlyphs">blurred vision</text>
        <text x="288" y="688" font-size="115" font-weight="900" fill="var(--red)"
              textLength="496" lengthAdjust="spacingAndGlyphs">redness..</text>
      </g>

      <circle class="device-photo" role="img" aria-label="Photo of the dry eye treatment device"
              cx="160" cy="755" r="105" fill="url(#devicePhoto)" stroke="var(--yellow)" stroke-width="5"/>

      <g class="now-badge">
        <circle cx="513" cy="818" r="64" fill="var(--ink)"/>
        <text x="513" y="830" text-anchor="middle" font-family="Montserrat, sans-serif"
              font-size="34" font-weight="600" fill="var(--white)">NOW</text>
      </g>
    </svg>

    <section class="offer">
      <p class="offer-lead">There is a quick, comfortable and affordable procedure offering relief to</p>
      <p class="offer-focus">Dry eye.</p>
      <hr class="offer-rule">
      <p class="offer-cta">Schedule your dry eye treatment today.</p>
    </section>

    <div class="brand">Irisvale<span class="brand-sub">Optometry</span></div>
  </main>
</body>
</html>
```